Office Stationary and Business Card package

I need a new fresh looking business card and stationary design. "I need to refresh and update my Stationary and Business card appearance.

We are a family dental practice that handles all phases of dentistry including cosmetic, emergency and implant restoration We like the use of Blue and Grey in the design. i would like to include my website address and Phone numbers on the new project as well as a choice of different back sides to business cards which might include a map, appointment information, or blank depending on the particular card. The business cards should allow for the inclusion of another persons name and title in some location.

Information to be included in stationery:

Gordon T Vallow DMD, FAIDS
A Professional Dental Corporation (this needs to be
somewhere on the stationary and business cards)
48610 Marlow Avenue
Linden Falls, OR 97381
PHONE: (562) 471-3095
WEBSITE: www.gordonvallowdmd-example.com

Designs need to be Vibrant, Professional and Clean.
Colors to use: Blue, Grey and White colors.

I currently do not have an existing logo. I would like something simply, similar to the attached.

```html
<!DOCTYPE html>
<html lang="en">
<head>
<meta charset="utf-8">
<title>Gordon T Vallow DMD – Stationery</title>
<link rel="stylesheet" href="https://fonts.googleapis.com/css2?family=Open+Sans:ital,wght@0,400;0,600;1,400&display=swap">
<style>
  :root {
    --brand-blue: #3a78c2;
    --swoosh: #c9d3ee;
    --text-grey: #7d7f84;
    --text-dark: #2d2f33;
    --line-grey: #dcdcdc;
    --paper: #ffffff;
    --backdrop: #f3f4f6;
  }
  * { box-sizing: border-box; margin: 0; padding: 0; }
  html, body { width: 1200px; height: 798px; overflow: hidden; }
  body {
    background: var(--backdrop);
    font-family: "Open Sans", Arial, sans-serif;
    position: relative;
  }
  .swoosh-layer { position: absolute; inset: 0; width: 100%; height: 100%; }
  .swoosh-layer path { fill: var(--swoosh); }

  .brand-mark { display: flex; align-items: center; gap: 8px; color: var(--brand-blue); font-weight: 400; white-space: nowrap; }
  .brand-mark__dot { width: 18px; height: 18px; border-radius: 50%; background: var(--brand-blue); }

  /* Business card */
  .business-card {
    position: absolute; left: 50px; top: 250px;
    width: 520px; height: 300px;
    background: var(--paper);
    box-shadow: 0 2px 10px rgba(0,0,0,.12);
    overflow: hidden;
  }
  .business-card .brand-mark { position: absolute; left: 36px; top: 128px; font-size: 22px; }
  .card-contact {
    position: absolute; right: 30px; top: 26px;
    text-align: right; color: var(--text-grey); font-size: 12px; line-height: 1.45;
  }
  .card-identity { position: absolute; left: 178px; top: 120px; white-space: nowrap; }
  .card-identity__name { color: var(--brand-blue); font-size: 20px; line-height: 1.3; }
  .card-identity__tagline { color: var(--text-grey); font-size: 13px; line-height: 1.3; }
  .card-address {
    position: absolute; left: 36px; bottom: 26px;
    color: var(--text-grey); font-size: 12.5px; word-spacing: 2px; white-space: nowrap;
  }
  .card-address .sep { margin: 0 9px; }

  /* Letterhead */
  .letterhead {
    position: absolute; left: 650px; top: 40px;
    width: 500px; height: 720px;
    background: var(--paper);
    box-shadow: 0 2px 12px rgba(0,0,0,.12);
    overflow: hidden;
  }
  .letterhead .brand-mark { position: absolute; left: 58px; top: 72px; font-size: 24px; }
  .letterhead-address {
    position: absolute; right: 52px; top: 38px;
    text-align: right; color: var(--text-grey); font-size: 12.5px; line-height: 1.35;
  }
  .letter-salutation { position: absolute; left: 90px; top: 186px; font-size: 10px; color: var(--text-dark); }
  .letter-body { position: absolute; left: 66px; top: 228px; width: 400px; }
  .letter-line { display: flex; gap: 10px; margin-bottom: 12px; }
  .letter-line span { height: 7px; background: var(--line-grey); display: block; }
  .letter-closing { position: absolute; left: 74px; top: 556px; font-size: 10px; color: var(--text-dark); }
  .letter-signature { position: absolute; left: 74px; top: 596px; font-size: 14px; color: var(--text-dark); }
  .letter-tagline {
    position: absolute; left: 130px; top: 630px;
    color: var(--brand-blue); font-size: 16px; font-style: italic;
  }
  .letter-contact { position: absolute; left: 130px; top: 662px; font-size: 10.5px; color: var(--text-grey); white-space: nowrap; }
  .letter-contact .sep { margin: 0 12px; }
</style>
</head>
<body>

  <section class="business-card">
    <svg class="swoosh-layer" viewBox="0 0 520 300" aria-hidden="true">
      <path d="M150 88 C 260 80 380 60 520 0 L520 10 C 390 70 270 92 150 88 Z"/>
      <path d="M0 272 C 140 185 330 165 520 162 L520 172 C 330 176 150 200 0 284 Z"/>
    </svg>
    <div class="card-contact">
      <div>www.gordonvallowdmd-example.com</div>
      <div>(541) 471-3095</div>
    </div>
    <div class="brand-mark"><span class="brand-mark__dot"></span>Vallow</div>
    <div class="card-identity">
      <div class="card-identity__name">Gordon T Vallow DMD, FAIDS</div>
      <div class="card-identity__tagline">A Professional Dental Corporation</div>
    </div>
    <div class="card-address">48610 Marlow Avenue<span class="sep">|</span>Linden Falls<span class="sep">|</span>OR<span class="sep">|</span>97381</div>
  </section>

  <section class="letterhead">
    <svg class="swoosh-layer" viewBox="0 0 500 720" aria-hidden="true">
      <path d="M270 0 C 290 70 360 110 500 108 L500 116 C 350 118 278 76 262 0 Z"/>
      <path d="M30 548 C 140 480 300 470 380 540 C 430 590 460 660 480 720 L468 720 C 448 660 420 600 372 552 C 300 488 150 500 30 556 Z"/>
    </svg>
    <div class="brand-mark"><span class="brand-mark__dot"></span>Vallow</div>
    <div class="letterhead-address">48610 Marlow Avenue<br>Linden Falls, OR<br>97381</div>
    <p class="letter-salutation">Dear Sir/Madam,</p>
    <div class="letter-body">
      <div class="letter-line"><span style="width:290px"></span><span style="width:100px"></span></div>
      <div class="letter-line"><span style="width:190px"></span><span style="width:200px"></span></div>
      <div class="letter-line"><span style="width:100px"></span><span style="width:290px"></span></div>
      <div class="letter-line"><span style="width:120px"></span><span style="width:200px"></span><span style="width:60px"></span></div>
      <div class="letter-line"><span style="width:390px"></span></div>
      <div class="letter-line"><span style="width:210px"></span><span style="width:180px"></span></div>
      <div class="letter-line"><span style="width:80px"></span><span style="width:300px"></span></div>
      <div class="letter-line"><span style="width:240px"></span><span style="width:150px"></span></div>
      <div class="letter-line"><span style="width:150px"></span><span style="width:80px"></span><span style="width:150px"></span></div>
      <div class="letter-line"><span style="width:270px"></span><span style="width:120px"></span></div>
      <div class="letter-line"><span style="width:160px"></span><span style="width:230px"></span></div>
      <div class="letter-line"><span style="width:230px"></span><span style="width:160px"></span></div>
    </div>
    <p class="letter-closing">Your Sincerely</p>
    <p class="letter-signature">Gordon T Vallow DMD, FAIDS</p>
    <p class="letter-tagline">A Professional Dental Corporation</p>
    <p class="letter-contact">(541) 471-3095<span class="sep">|</span>www.gordonvallowdmd-example.com</p>
  </section>

</body>
</html>
```